Harold Brisk Mechanical business cards

We need business cards designed for "Harold Brisk Mechanical" "Mechanical & Electrical Contractors" "Specializing in Service & Installation"
"Cooling, Heating, Service, Installations, Residential, Commercial"

```html
<!DOCTYPE html>
<html lang="en">
<head>
<meta charset="utf-8">
<title>Harold Brisk Mechanical – Business Cards</title>
<link href="https://fonts.googleapis.com/css2?family=Roboto:wght@300;400;500;700&family=Roboto+Condensed:wght@400;700&display=swap" rel="stylesheet">
<style>
  :root {
    --bg: #e9e6e1;
    --paper: #ffffff;
    --ink: #1d1d1d;
    --grey: #5a5a5a;
    --rule: #9a9a9a;
    --red: #e8262f;
    --night: #1c1c1c;
  }
  * { box-sizing: border-box; margin: 0; padding: 0; }
  html, body { width: 1200px; height: 768px; overflow: hidden; background: var(--bg); }
  body { position: relative; font-family: "Roboto", Arial, sans-serif; }

  .card {
    position: absolute;
    top: 235px;
    width: 520px;
    height: 298px;
    box-shadow: 0 6px 18px rgba(0,0,0,.18);
    overflow: hidden;
  }

  /* Front */
  .card--front { left: 50px; background: var(--paper); }
  .brand { position: absolute; left: 36px; top: 78px; display: flex; align-items: center; gap: 14px; }
  .brand__square { width: 48px; height: 48px; background: var(--red); }
  .brand__name {
    font-family: "Roboto Condensed", Arial, sans-serif;
    font-weight: 700; font-size: 22px; line-height: 1.05;
    color: var(--ink); text-transform: uppercase; width: 170px;
  }
  .person { position: absolute; right: 36px; top: 46px; text-align: right; }
  .person__name {
    font-family: "Roboto Condensed", Arial, sans-serif;
    font-weight: 700; font-size: 22px; color: var(--red); text-transform: uppercase;
  }
  .person__role {
    font-family: "Roboto Condensed", Arial, sans-serif;
    font-size: 13px; color: var(--ink); text-transform: uppercase; letter-spacing: .5px;
    border-bottom: 1px solid var(--rule); padding-bottom: 8px; width: 230px; margin-left: auto;
  }
  .address { position: absolute; right: 36px; top: 122px; text-align: right; font-size: 12.5px; line-height: 1.55; color: var(--grey); font-weight: 300; }
  .contacts { position: absolute; left: 36px; bottom: 34px; border-top: 1px solid var(--rule); padding-top: 10px; width: 260px; list-style: none; }
  .contacts li { display: flex; align-items: center; gap: 10px; font-size: 12.5px; line-height: 1.6; color: var(--grey); }
  .contacts svg { width: 12px; height: 12px; flex: none; }
  .front-band { position: absolute; left: 0; bottom: 0; width: 100%; height: 8px; background: var(--red); }
  .front-band::before { content: ""; position: absolute; left: 0; top: 0; width: 120px; height: 100%; background: var(--night); }

  /* Back */
  .card--back { left: 630px; background: var(--night); }
  .services { position: absolute; left: 30px; top: 28px; list-style: none; color: #fff; font-size: 13px; line-height: 1.55; }
  .services li::before { content: "•"; margin-right: 8px; }
  .back-panel {
    position: absolute; right: 0; bottom: 0; width: 320px; height: 170px; background: var(--paper);
    display: flex; align-items: center; justify-content: center; padding: 0 24px;
  }
  .back-panel__name {
    font-family: "Roboto Condensed", Arial, sans-serif; font-weight: 700; font-size: 28px; line-height: 1.1;
    color: var(--ink); text-transform: uppercase; text-align: center;
  }
</style>
</head>
<body>

<section class="card card--front">
  <div class="brand">
    <span class="brand__square"></span>
    <span class="brand__name">Harold Brisk Mechanical</span>
  </div>

  <div class="person">
    <p class="person__name">Evan Marlow</p>
    <p class="person__role">CEO/Founder</p>
  </div>

  <address class="address">
    412 Cedar Hollow Road<br>
    Fairbanks, Alaska 99701<br>
    www.hbmech-works.com
  </address>

  <ul class="contacts">
    <li>
      <svg viewBox="0 0 12 12"><path d="M3 1l2 2-1 1.5c.6 1.3 1.6 2.3 2.9 2.9L8.4 6l2 2-1.2 1.6C5.5 9.4 2.4 6.3 2 2.8z" fill="var(--red)"/></svg>
      907 555 0148
    </li>
    <li>
      <svg viewBox="0 0 12 12"><rect x="2" y="2.5" width="8" height="7" fill="none" stroke="var(--red)" stroke-width="1.4"/></svg>
      907 555 0172
    </li>
    <li>
      <svg viewBox="0 0 12 12"><rect x="2" y="1.5" width="8" height="4" fill="var(--red)"/><rect x="1.5" y="6.5" width="9" height="4" fill="var(--red)"/></svg>
      907 555 0193
    </li>
    <li>
      <svg viewBox="0 0 12 12"><rect x="1" y="1" width="10" height="10" fill="var(--red)"/><path d="M3 6l2 2 4-4" stroke="#fff" stroke-width="1.4" fill="none"/></svg>
      evan@hbmech-works.com
    </li>
  </ul>

  <div class="front-band"></div>
</section>

<section class="card card--back">
  <ul class="services">
    <li>Cooling</li>
    <li>Heating</li>
    <li>Service</li>
    <li>Installations</li>
    <li>Residential</li>
    <li>Commercial</li>
  </ul>
  <div class="back-panel">
    <p class="back-panel__name">Harold Brisk Mechanical</p>
  </div>
</section>

</body>
</html>
```